Web Design Project

We wish to create a web based logistics exchange for heavy machinery and equipment catering to the mining, oil, gas and infrastructure industries. Customers interested in shipping equipment can post a load on the site and this would then be auctioned off through an online auction to prospective transport providers.Payments would be through direct bank transfer,zenu, plumtender etc.
Both shippers and transport providers gain access via membership.
When a load is posted it would appear on the map indicating its location.Transport providers click on the icon of this map to access information of the pick up and delivery details as well as the load description.
The site would also have links to transport departments and equipment specification sites.
Advertising and merchandising are the other areas of revenue through the site

Target Market(s)

Shippers from Machinery Auction centres and Transport companies

Industry/Entity Type

Catering

Requirements
Must have
• The Logo of the company. The file is attached.

```html
<!DOCTYPE html>
<html lang="en">
<head>
<meta charset="utf-8">
<title>Haulward Freight – Dashboard</title>
<link href="https://fonts.googleapis.com/css2?family=PT+Sans:wght@400;700&display=swap" rel="stylesheet">
<style>
:root{
  --bg:#f1f1f1;
  --panel:#fafafa;
  --panel-head:#ececec;
  --line:#dddddd;
  --text:#555555;
  --muted:#8a8a8a;
  --dark:#333333;
  --blue:#1565a8;
  --blue-dark:#0d4f88;
  --blue-light:#2f8ad3;
  --footer:#e7e7e7;
  --icon:#3c3f44;
}
*{box-sizing:border-box;margin:0;padding:0}
html,body{width:1024px;height:1200px;overflow:hidden}
body{background:var(--bg);font-family:"PT Sans",Arial,sans-serif;font-size:10.5px;color:var(--text);border-top:3px solid #222;position:relative}
a{color:inherit;text-decoration:none}
svg.ico{width:13px;height:13px;fill:var(--icon);vertical-align:middle;margin-right:4px}

.site-header{position:absolute;top:0;left:102px;width:820px;height:100px}
.brand{position:absolute;top:28px;left:0;display:flex;align-items:center;gap:8px}
.brand-mark{width:26px;height:26px;border-radius:50%;background:var(--blue)}
.brand-name{font-size:20px;font-weight:700;color:var(--dark);letter-spacing:.5px}
.welcome{position:absolute;top:40px;right:156px;font-weight:700;font-size:11.5px;color:var(--dark)}
.search{position:absolute;top:34px;right:10px;width:133px;height:22px;border:1px solid #c9c9c9;border-radius:11px;background:#fff}
.search span{position:absolute;right:2px;top:2px;width:16px;height:16px;border-radius:50%;background:var(--blue-light)}
.main-nav{position:absolute;top:66px;right:10px;display:flex;gap:27px;font-size:11.5px;color:var(--text)}
.main-nav .active{font-weight:700;color:var(--dark)}

.tabs{position:absolute;top:100px;left:102px;width:820px;height:33px;background:#eeeeee;border:1px solid var(--line);border-radius:3px;display:flex}
.tab{width:102px;border-right:1px solid var(--line);display:flex;align-items:center;justify-content:center;font-weight:700;font-size:11.5px;color:#999;position:relative}
.tab.active{background:var(--blue);color:#fff;border-radius:3px 0 0 3px;width:101px}
.badge{position:absolute;top:-8px;right:14px;width:13px;height:13px;border-radius:50%;background:var(--blue-light);color:#fff;font-size:8px;display:flex;align-items:center;justify-content:center}
.badge.light{background:#e6eef6;color:var(--blue);width:10px;height:10px;font-size:7px;top:-6px}

.panel{position:absolute;background:var(--panel);border:1px solid var(--line);border-radius:3px}
.panel-title{height:31px;background:var(--panel-head);border-bottom:1px solid var(--line);font-weight:700;font-size:13px;color:#444;padding:7px 10px}
.shipments{top:139px;left:102px;width:469px;height:515px}
.pending{top:661px;left:102px;width:469px;height:136px}
.recommended{top:804px;left:102px;width:469px;height:159px}
.details{top:139px;left:579px;width:343px;height:824px}

.row{display:grid;grid-template-columns:62px 212px 76px 49px 1fr;align-items:center;height:26.4px;border-bottom:1px solid #e8e8e8;padding-left:9px;margin:0 4px 0 1px}
.row.head{height:30px;font-weight:700;color:#444;border-bottom:0}
.row.head span:nth-child(2){padding-left:2px}
.row.selected{background:var(--blue);color:#fff;margin:0;padding-left:10px}
.row.selected svg.ico{fill:#fff}
.row svg.ico{width:14px;height:14px;margin-right:6px}
.pager{padding:8px 11px;color:#444}
.more{padding:6px 11px;font-weight:700;font-size:10px;color:#666}

.action{height:26px;border-bottom:1px solid #e8e8e8;display:flex;align-items:center;padding-left:9px;margin:0 2px}
.action svg.ico{width:15px;height:15px;margin-right:5px}

.map{position:absolute;top:41px;left:6px;width:330px;height:232px;background:linear-gradient(110deg,#dfe6cf 0%,#cfdbb6 45%,#b9cd9c 60%,#a9c3dc 72%,#9dbcd8 100%)}
.subtabs{position:absolute;top:273px;left:6px;width:330px;height:24px;display:flex;background:#f0f0f0;border:1px solid var(--line)}
.subtabs span{flex:1;display:flex;align-items:center;justify-content:center;font-weight:700;color:#999;border-right:1px solid var(--line)}
.subtabs .on{background:var(--blue);color:#fff}
.job-title{position:absolute;top:310px;left:10px;right:10px;padding-bottom:9px;border-bottom:1px solid var(--line);font-weight:700;color:#444;font-size:11px}
.facts{position:absolute;top:337px;left:10px;width:325px;display:grid;grid-template-columns:62px 1fr;line-height:16.2px}
.facts dd svg.ico{width:14px;height:14px;margin-right:2px}
.facts dd.copytext{white-space:nowrap}
.actions{position:absolute;top:793px;left:71px;display:flex;gap:8px}
.btn{width:109px;height:21px;border:1px solid #c9c9c9;border-radius:2px;background:linear-gradient(#fff,#e9e9e9);display:flex;align-items:center;justify-content:center;font-weight:700;color:#444;font-size:10.5px}

.site-footer{position:absolute;top:983px;left:0;width:1024px;height:217px;background:var(--footer)}
.fcol{position:absolute;top:27px;line-height:17.8px;color:var(--muted)}
.fcol h4{font-weight:400;color:var(--dark);font-size:10.5px}
.newsletter{position:absolute;top:47px;left:724px;width:188px;height:21px;border:1px solid #c9c9c9;border-radius:11px;background:#fff;color:#999;padding:3px 10px}
.newsletter span{position:absolute;right:2px;top:2px;width:15px;height:15px;border-radius:50%;background:var(--blue-light)}
.follow{position:absolute;top:79px;left:724px;color:var(--dark)}
.social{position:absolute;top:100px;left:724px;display:flex;gap:5px}
.social span{width:26px;height:26px;border-radius:3px}
.copy{position:absolute;top:177px;left:111px;color:var(--muted)}
.copy a{color:var(--dark)}
</style>
</head>
<body>
<svg width="0" height="0" style="position:absolute">
  <defs>
    <symbol id="i-fire" viewBox="0 0 16 16"><path d="M8 1c1 3 5 5 5 9a5 5 0 0 1-10 0c0-2 1-3 2-4 0 2 1 3 2 3-1-3 0-6 1-8z"/></symbol>
    <symbol id="i-truck" viewBox="0 0 16 16"><path d="M1 4h9v7H1zM10 6h3l2 3v2h-5z"/><circle cx="4" cy="12.5" r="1.7"/><circle cx="12" cy="12.5" r="1.7"/></symbol>
    <symbol id="i-cart" viewBox="0 0 16 16"><path d="M1 2h3l1 2h10l-2 6H6L4 4H3z"/><circle cx="6.5" cy="13" r="1.5"/><circle cx="12" cy="13" r="1.5"/></symbol>
    <symbol id="i-cycle" viewBox="0 0 16 16"><path d="M13 3v4H9l1.6-1.6A4 4 0 0 0 4 8H2a6 6 0 0 1 10-4.4zM3 13V9h4l-1.6 1.6A4 4 0 0 0 12 8h2a6 6 0 0 1-10 4.4z"/></symbol>
    <symbol id="i-box" viewBox="0 0 16 16"><path d="M1 3h14v11H1zm2 2v7h10V5z"/><path d="M4 6l4 3 4-3v2l-4 3-4-3z"/></symbol>
    <symbol id="i-bars" viewBox="0 0 16 16"><path d="M1 9h3v6H1zM6 6h3v9H6zM11 3h3v12h-3z"/><circle cx="2.5" cy="5" r="1.5"/><circle cx="7.5" cy="2.5" r="1.5"/></symbol>
    <symbol id="i-badge" viewBox="0 0 16 16"><path d="M8 1a6 6 0 1 0 0.01 0zm0 3a3 3 0 1 1-0.01 0z"/></symbol>
    <symbol id="i-tick" viewBox="0 0 16 16"><path d="M1 8l2-2 3 3 7-7 2 2-9 9z"/></symbol>
  </defs>
</svg>

<header class="site-header">
  <a class="brand" href="#"><span class="brand-mark"></span><span class="brand-name">HAULWARD FREIGHT</span></a>
  <div class="welcome">Welcome Dale Cartwright</div>
  <div class="search"><span></span></div>
  <nav class="main-nav"><a class="active" href="#">Home</a><a href="#">About Us</a><a href="#">How It Works</a><a href="#">Contact Us</a><a href="#">FAQs</a></nav>
</header>

<nav class="tabs">
  <a class="tab active" href="#">Dashboard</a>
  <a class="tab" href="#">My Profile</a>
  <a class="tab" href="#">Notifications<span class="badge light" style="right:44px">3</span></a>
  <a class="tab" href="#">Messages<span class="badge">5</span></a>
  <a class="tab" href="#">Payments</a>
</nav>

<section class="panel shipments">
  <h2 class="panel-title">Shipment Projects</h2>
  <div class="row head"><span>Project ID</span><span>Description</span><span>Category</span><span>Status</span><span>Time Left</span></div>
  <div class="row"><span>52152</span><span>HX3920EE Melborne to Sydney</span><span><svg class="ico"><use href="#i-fire"/></svg><svg class="ico"><use href="#i-truck"/></svg><svg class="ico"><use href="#i-cycle"/></svg></span><span>Open</span><span>4 Days</span></div>
  <div class="row"><span>52152</span><span>HX3920EE Melborne to Sydney</span><span><svg class="ico"><use href="#i-box"/></svg><svg class="ico"><use href="#i-cart"/></svg></span><span>Open</span><span>4 Days</span></div>
  <div class="row"><span>52152</span><span>HX3920EE Melborne to Sydney</span><span><svg class="ico"><use href="#i-fire"/></svg><svg class="ico"><use href="#i-cart"/></svg><svg class="ico"><use href="#i-truck"/></svg></span><span>Open</span><span>4 Days</span></div>
  <div class="row"><span>52152</span><span>HX3920EE Melborne to Sydney</span><span><svg class="ico"><use href="#i-cycle"/></svg><svg class="ico"><use href="#i-cart"/></svg></span><span>Open</span><span>4 Days</span></div>
  <div class="row"><span>52152</span><span>HX3920EE Melborne to Sydney</span><span><svg class="ico"><use href="#i-box"/></svg><svg class="ico"><use href="#i-truck"/></svg></span><span>Open</span><span>4 Days</span></div>
  <div class="row"><span>52152</span><span>HX3920EE Melborne to Sydney</span><span><svg class="ico"><use href="#i-box"/></svg></span><span>Open</span><span>4 Days</span></div>
  <div class="row selected"><span>52152</span><span>HX3920EE Melborne to Sydney</span><span><svg class="ico"><use href="#i-fire"/></svg><svg class="ico"><use href="#i-truck"/></svg><svg class="ico"><use href="#i-cycle"/></svg></span><span>Open</span><span>4 Days</span></div>
  <div class="row"><span>52152</span><span>HX3920EE Melborne to Sydney</span><span><svg class="ico"><use href="#i-fire"/></svg><svg class="ico"><use href="#i-truck"/></svg><svg class="ico"><use href="#i-cycle"/></svg></span><span>Open</span><span>4 Days</span></div>
  <div class="row"><span>52152</span><span>HX3920EE Melborne to Sydney</span><span><svg class="ico"><use href="#i-box"/></svg><svg class="ico"><use href="#i-cart"/></svg></span><span>Open</span><span>4 Days</span></div>
  <div class="row"><span>52152</span><span>HX3920EE Melborne to Sydney</span><span><svg class="ico"><use href="#i-fire"/></svg><svg class="ico"><use href="#i-cart"/></svg><svg class="ico"><use href="#i-truck"/></svg></span><span>Open</span><span>4 Days</span></div>
  <div class="row"><span>52152</span><span>HX3920EE Melborne to Sydney</span><span><svg class="ico"><use href="#i-cycle"/></svg><svg class="ico"><use href="#i-cart"/></svg></span><span>Open</span><span>4 Days</span></div>
  <div class="row"><span>52152</span><span>HX3920EE Melborne to Sydney</span><span><svg class="ico"><use href="#i-box"/></svg><svg class="ico"><use href="#i-truck"/></svg></span><span>Open</span><span>4 Days</span></div>
  <div class="row"><span>52152</span><span>HX3920EE Melborne to Sydney</span><span><svg class="ico"><use href="#i-box"/></svg></span><span>Open</span><span>4 Days</span></div>
  <div class="row"><span>52152</span><span>HX3920EE Melborne to Sydney</span><span><svg class="ico"><use href="#i-fire"/></svg><svg class="ico"><use href="#i-truck"/></svg><svg class="ico"><use href="#i-cycle"/></svg></span><span>Closed</span><span>4 Days</span></div>
  <div class="row"><span>52152</span><span>HX3920EE Melborne to Sydney</span><span><svg class="ico"><use href="#i-box"/></svg><svg class="ico"><use href="#i-cart"/></svg></span><span>Open</span><span>4 Days</span></div>
  <div class="row"><span>52152</span><span>HX3920EE Melborne to Sydney</span><span><svg class="ico"><use href="#i-fire"/></svg><svg class="ico"><use href="#i-cart"/></svg><svg class="ico"><use href="#i-truck"/></svg></span><span>Open</span><span>4 Days</span></div>
  <div class="pager">1 2 3 4 5 ... Next &gt;</div>
</section>

<section class="panel pending">
  <h2 class="panel-title">My Pending Actions</h2>
  <div class="action"><svg class="ico"><use href="#i-bars"/></svg>Get Endorsed and move up the ranks.</div>
  <div class="action"><svg class="ico"><use href="#i-badge"/></svg>You have 7 pending Proposals</div>
  <div class="action"><svg class="ico"><use href="#i-tick"/></svg>Verify your credit card to enjoy faster payments</div>
  <div class="more">more&gt;</div>
</section>

<section class="panel recommended">
  <h2 class="panel-title">Recommended</h2>
  <div class="row"><span>52152</span><span>HX3920EE Melborne to Sydney</span><span><svg class="ico"><use href="#i-fire"/></svg><svg class="ico"><use href="#i-truck"/></svg><svg class="ico"><use href="#i-cycle"/></svg></span><span>Open</span><span>4 Days</span></div>
  <div class="row"><span>52152</span><span>HX3920EE Melborne to Sydney</span><span><svg class="ico"><use href="#i-box"/></svg><svg class="ico"><use href="#i-cart"/></svg></span><span>Open</span><span>4 Days</span></div>
  <div class="row"><span>52152</span><span>HX3920EE Melborne to Sydney</span><span><svg class="ico"><use href="#i-fire"/></svg><svg class="ico"><use href="#i-cart"/></svg><svg class="ico"><use href="#i-truck"/></svg></span><span>Open</span><span>4 Days</span></div>
  <div class="row"><span>52152</span><span>HX3920EE Melborne to Sydney</span><span><svg class="ico"><use href="#i-cycle"/></svg><svg class="ico"><use href="#i-cart"/></svg></span><span>Open</span><span>4 Days</span></div>
  <div class="more">more&gt;</div>
</section>

<section class="panel details">
  <h2 class="panel-title">Project Details</h2>
  <div class="map" role="img" aria-label="Road map of south-east Australia showing the route from Melbourne to Sydney"></div>
  <div class="subtabs"><span class="on">Overview</span><span>Pickup</span><span style="border-right:0">Destination</span></div>
  <div class="job-title">HX3920EE Melborne to Sydney</div>
  <dl class="facts">
    <dt>Posted by</dt><dd>Ray Contos</dd>
    <dt>Category</dt><dd><svg class="ico"><use href="#i-fire"/></svg><svg class="ico"><use href="#i-truck"/></svg><svg class="ico"><use href="#i-cycle"/></svg></dd>
    <dt>Status</dt><dd>Open</dd>
    <dt>Time Left</dt><dd>5 Days 4 Hours</dd>
    <dt>Pickup</dt><dd>34, Malibu Industries<br>New Town<br>Melbourne&nbsp;&nbsp;&nbsp;236325</dd>
    <dt>Destination</dt><dd>Department of Physics<br>132A, Adress Impsum<br>Community Centerpen<br>Sydney</dd>
    <dt>Weight</dt><dd>4,231 Kg</dd>
    <dt>Volume</dt><dd>31 m³</dd>
    <dt>Cargo</dt><dd>HX3920EE Excavator</dd>
    <dt>Details</dt><dd class="copytext">This is the sample version&nbsp; of Lorem Ipsum.<br>Proin gravida nibh vel velit auctor aliquet. Aenean s<br>ollicitudin, lorem quis bibendum auctor, nisi elit<br>consequat ipsum, nec sagittis sem nibh id elitor, nisi<br>elit consequat ipsum, nec sagittis sem nibh id elit.<br>Duis sed odio sit amet nibh vulputate cursus a sit amet<br>mauris. Morbi accumsan ipsum velit. Nam nec tellus<br>a odio tincidunt auctor a ornare odio.<br><br>Sed non&nbsp; mauris vitae erat consequat auctor eu in elit.<br>Class aptent taciti sociosqu ad litora torquent per<br>conubia nostra, per inceptos himenaeos. Mauris in erat<br>justo. Nullam ac urna eu felis dapibus condimentum sit<br>amet a augue.</dd>
  </dl>
  <div class="actions"><a class="btn" href="#">More Info</a><a class="btn" href="#">Bid for this Job</a></div>
</section>

<footer class="site-footer">
  <div class="fcol" style="left:111px"><h4>Why Us</h4>Features<br>Pricing<br>Site Gallery<br>Demo Video<br>Clients<br>Testimonials</div>
  <div class="fcol" style="left:213px"><h4>Company</h4>About Us<br>Press<br>Careers<br>Contact Us<br>Partner with Us</div>
  <div class="fcol" style="left:316px"><h4>Support</h4>Help<br>Contact Support<br>Video Tutorials<br>Privacy Policy<br>Terms of Service<br>Report Abuse</div>
  <div class="fcol" style="left:416px"><h4>Community</h4>Blog<br>Forums<br>Affiliates</div>
  <div class="fcol" style="left:520px"><h4>Contact Us</h4>14 Quarry Lane<br>Gravida nibh vel velit auctor aliquet<br>Aenean sollicitudin<br>Mellborne<br><br>hello@haulward.example<br>(555) 014 2207</div>
  <div class="fcol" style="left:724px"><h4>Subscribe Newsletter</h4></div>
  <div class="newsletter">email address<span></span></div>
  <div class="follow">Follow Us</div>
  <div class="social"><span style="background:#4a6ea9"></span><span style="background:#5bbbe6"></span><span style="background:#3b3b3b"></span><span style="background:#d9262f"></span></div>
  <div class="copy">Copyright 2013. All rights reserved. <a href="#">Privacy Policy</a> | <a href="#">Terms of Service</a></div>
</footer>
</body>
</html>
```